Personal Trainer. Ruvane PT. Needs poster to attract clients.

I need a poster to attract clients to my business Ruvane PT.
The demographic I am targeting is 30-45 year old overweight women and men. I would like some gym pictures incorporated. (these should not be pics of athletes/super fit body types)These are up to you. Please note my target market as super fit models would not be appropriate.
I am fond of the black background but I am open to change.

I wanted my contact details to be
Phone number- 0427 380 615
and
Facebook- Ruvane PT.
No email, website or street address please
I would like a small picture of myself near the contact details but do not want my photo to be a feature.

Attached is my old poster design.
****PLEASE NOTE CHANGES ABOVE****

Target Market(s)

Both overweight women and men 30-45 years old

Industry/Entity Type

Business

Requirements
Should not have
• Street address
• Web address
• Pics of super fit athletes

```html
<!DOCTYPE html>
<html lang="en">
<head>
<meta charset="utf-8">
<title>Ruvane PT – Stay Fit Poster</title>
<link rel="stylesheet" href="https://fonts.googleapis.com/css2?family=Archivo:ital,wght@0,900;1,900&family=Audiowide&family=Roboto+Slab:wght@800&family=PT+Sans:wght@700&family=Open+Sans:wght@600&display=swap">
<style>
  :root {
    --yellow: #f7d117;
    --orange: #e98a1f;
    --blue: #1b86c9;
    --blue-dark: #17508c;
    --ink: #232323;
    --grey-top: #5e5e5e;
    --grey-bottom: #3b3b3b;
    --white: #ffffff;
    --pink: #e8417e;
  }
  html, body { margin: 0; padding: 0; overflow: hidden; background: #222; }
  .poster {
    position: relative;
    width: 849px;
    height: 1200px;
    overflow: hidden;
    background: linear-gradient(180deg, var(--grey-top), var(--grey-bottom));
  }
  .poster-art { position: absolute; inset: 0; width: 849px; height: 1200px; }
  .headline { font-family: "Archivo", sans-serif; font-weight: 900; font-style: italic; fill: var(--ink); }
  .stay-fit { font-family: "Audiowide", sans-serif; fill: var(--white); stroke: var(--blue-dark); stroke-width: 6; paint-order: stroke; stroke-linejoin: round; }
  .services { font-family: "Roboto Slab", serif; font-weight: 800; fill: var(--white); }
  .trainer-name { font-family: "PT Sans", sans-serif; font-weight: 700; fill: var(--yellow); }
  .brand-name { font-family: "Archivo", sans-serif; font-weight: 900; fill: var(--yellow); }
  .contact-text { font-family: "Open Sans", sans-serif; font-weight: 600; fill: var(--white); }
</style>
</head>
<body>
<div class="poster">
  <svg class="poster-art" viewBox="0 0 849 1200" xmlns="http://www.w3.org/2000/svg">
    <defs>
      <linearGradient id="gymPhotoTone" x1="0" y1="0" x2="1" y2="1">
        <stop offset="0" stop-color="#8a8a88"/>
        <stop offset="0.35" stop-color="#c9a08e"/>
        <stop offset="0.55" stop-color="#a878c4"/>
        <stop offset="0.8" stop-color="#e6e6e2"/>
        <stop offset="1" stop-color="#f4f4f2"/>
      </linearGradient>
    </defs>

    <rect class="hero-photo" x="0" y="0" width="849" height="800" fill="url(#gymPhotoTone)" role="img" aria-label="Smiling woman in a purple tank top doing sit-ups in a bright gym"/>

    <polygon class="band-yellow" points="0,616 849,512 849,672 0,788" fill="var(--yellow)"/>
    <polygon class="band-orange-rule" points="0,780 849,664 849,674 0,790" fill="var(--orange)"/>
    <polygon class="band-blue" points="0,788 849,672 849,832 0,932" fill="var(--blue)"/>

    <g class="headline" transform="translate(52,668) rotate(-7)">
      <text x="0" y="0"><tspan font-size="36">YOUR </tspan><tspan font-size="68">FITNESS</tspan></text>
      <text x="40" y="64"><tspan font-size="36">IS YOUR </tspan><tspan font-size="74">HAPPINESS</tspan></text>
    </g>

    <g transform="translate(144,860) rotate(-7)">
      <text class="stay-fit" x="0" y="0" font-size="100" textLength="672" lengthAdjust="spacingAndGlyphs">STAY FIT...</text>
    </g>

    <g transform="translate(36,962) rotate(-7)">
      <text class="services" x="0" y="0" font-size="30" textLength="794" lengthAdjust="spacingAndGlyphs">•GYM •CARDIO •AEROBICS •WEIGHT LOSS •YOGA</text>
    </g>

    <text class="trainer-name" x="606" y="982" font-size="38" text-anchor="middle">DALE MORGAN</text>
    <text class="trainer-name" x="606" y="1016" font-size="24" text-anchor="middle">PERSONAL TRAINER</text>

    <rect class="brand-rule" x="364" y="1032" width="485" height="6" fill="var(--yellow)"/>
    <text class="brand-name" x="602" y="1112" font-size="70" text-anchor="middle">RUVANE PT</text>
    <rect class="brand-underline" x="384" y="1138" width="380" height="2" fill="var(--blue)"/>

    <circle class="trainer-portrait" cx="60" cy="1100" r="36" fill="#7b7470" stroke="#cfcfcf" stroke-width="3" role="img" aria-label="Small portrait of the trainer"/>

    <g class="phone-icon" transform="translate(110,1068)">
      <rect width="22" height="24" rx="4" fill="var(--pink)"/>
      <rect x="6" y="4" width="10" height="14" rx="1.5" fill="none" stroke="var(--white)" stroke-width="1.8"/>
      <circle cx="11" cy="20.5" r="1.2" fill="var(--white)"/>
    </g>
    <text class="contact-text" x="142" y="1090" font-size="30">0427 380 615</text>

    <rect class="social-marker" x="110" y="1110" width="22" height="24" rx="3" fill="var(--blue)"/>
    <text class="contact-text" x="142" y="1133" font-size="29">Ruvane PT</text>
  </svg>
</div>
</body>
</html>
```